WE RISE NOW - Personal Growth Seminar

The project is collaboration between Desmond Farrow and Marian Pelloway. It will combine the skills of both parties to launch an inspirational and motivation Personal Growth Seminar. We are looking for an e-flyer and a general design that we can use in our promotional work

The programme is a one day seminar which will show delegates how to

1) Kick start your life
2) Overcome obstacles and self sabotage
3) Take control of your future
4) Think bigger than you thought possible
5) Increase your confidence and self belief
6) Six steps to WE RISE NOW success

Our values for the seminar, that the eflyer should represent are:
Professional
Freedom
Nature (really important theme)
Fun
Honest
Balance
Integrity

We want to GRAB people's attention and then ENGAGE them into booking onto the seminar. We will send over details for the links to the seminar and phone numbers etc later, so they need to be incorporated. The seminar will be held in a hotel called The Hazelmere (nature and growth theme)

The one thing to remember is, to step back from the design and ask yourself would you book the seminar, based on what you see.

Our websites so you can see our current themes are www.marianpelloway.com and www.desmondfarrow.co.uk

Target Market(s)

Adults based in UK, between 25 and 50 years of age.

Industry/Entity Type

Hotel

Requirements
Must have
• Nature theme - growth
Fun but professional

Colours green but more vibrant like grass colour, nothing dull or washed out

Nice to have
• The picture will give you an idea but doesn't need to be used, it is just for guidance.

A Tree theme could be used - perhaps with the WE RISE NOW on the branches
Should not have
• Should not include cartoons

Gawdy colours or too much text

```html
<!DOCTYPE html>
<html lang="en">
<head>
<meta charset="utf-8">
<title>WE RISE NOW – Personal Growth Seminar</title>
<link href="https://fonts.googleapis.com/css2?family=Arimo:ital,wght@0,400;0,700;1,400&display=swap" rel="stylesheet">
<style>
  :root {
    --ink: #333333;
    --orange: #f7931e;
    --green: #66dd1f;
    --green-light: #9be870;
    --paper: #ffffff;
    --mist: #eef0ee;
    --photo-sky: #8c9a6a;
    --photo-deep: #4a5a2c;
    --photo-light: #c9d3a0;
  }
  * { box-sizing: border-box; margin: 0; padding: 0; }
  html, body { width: 850px; height: 1200px; overflow: hidden; }
  body {
    font-family: "Arimo", Arial, sans-serif;
    color: var(--ink);
    background: var(--paper);
  }
  .flyer {
    position: relative;
    width: 850px;
    height: 1200px;
    background: radial-gradient(ellipse at 30% 40%, var(--mist) 0%, var(--paper) 70%);
    overflow: hidden;
  }
  .title {
    position: absolute;
    top: 42px; left: 0; width: 850px;
    text-align: center;
    font-weight: 400;
    font-size: 104px;
    line-height: 1;
    letter-spacing: 0;
    white-space: nowrap;
    color: var(--ink);
  }
  .tagline {
    position: absolute;
    top: 165px; left: 25px;
    font-style: italic;
    font-size: 21px;
    white-space: nowrap;
  }
  .tagline .kind { color: var(--orange); }
  .tagline .hosts { color: var(--green); }
  .date {
    position: absolute;
    top: 197px; right: 25px;
    font-style: italic;
    font-size: 29px;
    letter-spacing: 1px;
    white-space: nowrap;
  }
  .rule-h {
    position: absolute;
    top: 237px; left: 0;
    width: 850px; height: 8px;
    background: var(--orange);
  }
  .rule-v {
    position: absolute;
    top: 237px; left: 370px;
    width: 10px; height: 382px;
    background: var(--orange);
  }
  .benefits {
    position: absolute;
    top: 268px; left: 20px;
    width: 345px;
    list-style: none;
    font-size: 22px;
    letter-spacing: 1.5px;
    line-height: 1.12;
  }
  .benefits li { margin-bottom: 25px; }
  .benefits b { font-weight: 700; }
  .hero-frame {
    position: absolute;
    top: 249px; left: 385px;
    width: 465px; height: 390px;
    background: var(--green-light);
  }
  .hero-photo {
    position: absolute;
    top: 256px; left: 389px;
    width: 461px; height: 362px;
    background:
      radial-gradient(circle at 52% 42%, #f4f0c0 0%, var(--photo-light) 12%, var(--photo-sky) 40%, var(--photo-deep) 100%);
  }
  .headline {
    position: absolute;
    top: 638px; left: 0; width: 850px;
    text-align: center;
    font-weight: 700;
    font-size: 92px;
    letter-spacing: 4px;
    line-height: 1;
    white-space: nowrap;
  }
  .register {
    position: absolute;
    top: 714px; left: 255px;
    display: flex; align-items: baseline; gap: 6px;
    white-space: nowrap;
  }
  .register .lead {
    font-weight: 700;
    font-size: 17px;
    letter-spacing: 1px;
  }
  .register .action {
    font-weight: 700;
    font-size: 50px;
    letter-spacing: 1px;
    line-height: 1;
    color: var(--green);
    text-decoration: none;
  }
  .speakers-heading {
    position: absolute;
    top: 760px; left: 35px;
    font-weight: 700;
    font-size: 46px;
    letter-spacing: 2.5px;
    line-height: 1;
    white-space: nowrap;
  }
  .speaker {
    position: absolute;
    top: 810px;
    width: 320px;
    text-align: center;
  }
  .speaker--marian { left: 55px; }
  .speaker--desmond { left: 467px; }
  .speaker-photo {
    width: 320px; height: 320px;
  }
  .speaker--marian .speaker-photo {
    background: linear-gradient(160deg, #f3f3f1 0%, #e6ddd6 55%, #e9b8a8 100%);
  }
  .speaker--desmond .speaker-photo {
    background: linear-gradient(160deg, #6e6a62 0%, #3a3733 55%, #1f1d1b 100%);
  }
  .speaker-name {
    margin-top: 10px;
    font-weight: 700;
    font-size: 27px;
    letter-spacing: 2px;
    white-space: nowrap;
  }
</style>
</head>
<body>
<main class="flyer">
  <h1 class="title">WE RISE NOW</h1>
  <p class="tagline"><span class="kind">PERSONAL GROWTH SEMINAR</span> <span class="hosts">With Desmond Farrow and Marian Pelloway</span></p>
  <p class="date">Thursday, June 30, 2011</p>

  <div class="rule-h"></div>
  <div class="rule-v"></div>

  <ul class="benefits">
    <li>GAIN CLEAR DIRECTION</li>
    <li>OVERCOME OBSTACLES</li>
    <li>OVERCOME SABOTAGING ACTIONS</li>
    <li>THINK BIGGER</li>
    <li>INCREASE CONFIDENCE</li>
    <li>RECOGNIZE <b>SIX WE RISE NOW</b> STEPS TO SUCCESS</li>
  </ul>

  <div class="hero-frame"></div>
  <div class="hero-photo" role="img" aria-label="A lone tree on a grassy hill with sunlight bursting through its branches under green-tinted clouds"></div>

  <h2 class="headline">ONE DAY ONLY!</h2>
  <p class="register"><span class="lead">CLICK HERE TO</span><a class="action" href="#">REGISTER NOW</a></p>

  <h2 class="speakers-heading">SEMINAR SPEAKERS</h2>

  <figure class="speaker speaker--marian">
    <div class="speaker-photo" role="img" aria-label="Portrait of speaker Marian Pelloway leaning against a white wall"></div>
    <figcaption class="speaker-name">MARIAN PELLOWAY</figcaption>
  </figure>

  <figure class="speaker speaker--desmond">
    <div class="speaker-photo" role="img" aria-label="Portrait of speaker Desmond Farrow smiling at a conference"></div>
    <figcaption class="speaker-name">DESMOND FARROW</figcaption>
  </figure>
</main>
</body>
</html>
```